Kelvane Plumbing Business cards

Company is Kelvane Plumbing.
name Dashel Morrowby, I am a plumber, drainer, gasfitter and roofer
Mobile: 0431 906 154
Email address: info@kelvaneplumbing.example (check out my website for some ideas)
Website: www.kelvaneplumbing.example
ABN: 82 916 203 471
LIC: 604517K

I am reliable all round plumber. I am a 24 hour emergency service. Kelvane Plumbing is a professional plumbing service in the Illawarra, South Coast, Southern Sydney and Southern Highland regions of NSW. We offer a 24 hour emergency service for piece of mind to our customers. Call us now to see how we can help you. Kelvane Plumbing approaches every job with attention to detail and excellent customer service. With our superior workmanship you can be confident that the job will be done right the first time around. You can rest assured with results that are guaranteed to last.

Target Market(s)

the general public

Contact Information for Business Card

look up website for some ideas something with similar colours to logo and new modern and to catch the eye.

Colors
fdfdfd
ffffff
000000
7f7f7f
aaaaaa
33a6d7
0492cd

Requirements
Must have
• all contact details
• company- Kelvane Plumbing
• name- Dashel Morrowby
• number mobile- 0431 906 154
• Email address- info@kelvaneplumbing.example
• Website- www.kelvaneplumbing.example
• ABN- 82 916 203 471
• LIC- 604517K

```html
<!DOCTYPE html>
<html lang="en">
<head>
<meta charset="utf-8">
<title>Kelvane Plumbing — Business Cards</title>
<link rel="stylesheet" href="https://fonts.googleapis.com/css2?family=Playfair+Display:wght@700&family=Titillium+Web:wght@300;400;600&display=swap">
<style>
  :root {
    --bg: #d9d3d4;
    --card-blue: #3a5f95;
    --card-shadow: rgba(30, 30, 40, 0.25);
    --ink-light: #f4f6fa;
    --ink-soft: #dfe6f0;
    --brand-blue: #33a6d7;
    --decor-grey: rgba(170, 170, 170, 0.45);
  }
  * { box-sizing: border-box; margin: 0; padding: 0; }
  html, body {
    width: 1200px; height: 886px; overflow: hidden;
    background: var(--bg);
  }
  .sheet {
    width: 1200px; height: 886px;
    display: flex; align-items: center; justify-content: center; gap: 40px;
  }
  .card {
    position: relative;
    width: 540px; height: 309px;
    background: var(--card-blue);
    box-shadow: 0 10px 28px var(--card-shadow);
    overflow: hidden;
    color: var(--ink-light);
    font-family: "Titillium Web", sans-serif;
  }
  .card__decor {
    position: absolute; top: 0; right: 14px;
    width: 74px; height: 190px;
    border-radius: 0 0 36px 36px;
    background: linear-gradient(180deg, var(--decor-grey), rgba(170,170,170,0.2));
    z-index: 0;
  }
  .card > *:not(.card__decor) { z-index: 1; }
  /* Front */
  .brand {
    position: absolute; left: 90px; top: 112px;
    display: flex; align-items: center; gap: 12px;
  }
  .brand__dot {
    width: 18px; height: 18px; border-radius: 50%;
    background: var(--brand-blue);
  }
  .brand__name {
    font-weight: 600; font-size: 30px; letter-spacing: 1px;
    color: var(--brand-blue);
    white-space: nowrap;
  }
  .registration {
    position: absolute; left: 38px; right: 38px; bottom: 26px;
    display: flex; justify-content: space-between;
    font-weight: 300; font-size: 17px; color: var(--ink-soft);
  }
  /* Back */
  .contact {
    position: absolute; left: 30px; right: 110px; top: 58px;
    text-align: center;
  }
  .contact__name {
    font-family: "Playfair Display", serif;
    font-weight: 700; font-size: 26px; line-height: 1.1;
  }
  .contact__role {
    font-family: "Playfair Display", serif;
    font-weight: 700; font-size: 14px; margin-top: 4px;
  }
  .contact__lines {
    list-style: none; margin-top: 14px;
    font-weight: 300; font-size: 19px; line-height: 1.3;
  }
  .emergency {
    position: absolute; left: 30px; right: 110px; bottom: 30px;
    text-align: center;
    font-weight: 300; font-size: 14px; letter-spacing: 0.5px;
    text-transform: uppercase; color: var(--ink-soft);
  }
</style>
</head>
<body>
<main class="sheet">
  <section class="card card--front">
    <div class="card__decor" role="img" aria-label="Faint pipe wrench decoration"></div>
    <div class="brand">
      <span class="brand__dot"></span>
      <span class="brand__name">Kelvane Plumbing</span>
    </div>
    <div class="registration">
      <span>LIC: 604517K</span>
      <span>ABN: 82 916 203 471</span>
    </div>
  </section>

  <section class="card card--back">
    <div class="card__decor" role="img" aria-label="Faint pipe wrench decoration"></div>
    <div class="contact">
      <h1 class="contact__name">Dashel Morrowby</h1>
      <p class="contact__role">Plumber, drainer, gasfitter and roofer</p>
      <ul class="contact__lines">
        <li>info@kelvaneplumbing.example</li>
        <li>kelvaneplumbing.example</li>
        <li>0431 906 154</li>
      </ul>
    </div>
    <p class="emergency">24 hour emergency service</p>
  </section>
</main>
</body>
</html>
```